Breezeway Comfort business cards design

Need a business card design for a Heating and Air Conditioning business. I need these items included.
Business name: Breezeway Comfort
Owner: Marcus Tollefsen
License # 2874590
Phone number # 555-382-4071
Email: breezewaycomfortair@mailvista.example
Sales
Service
Installation
Maintenance

Heating and Air Conditioning

Requirements
Must have
• Company name , license number , phone number , email

```html
<!DOCTYPE html>
<html lang="en">
<head>
<meta charset="utf-8">
<title>Breezeway Comfort — Business Cards</title>
<link rel="stylesheet" href="https://fonts.googleapis.com/css2?family=Montserrat:wght@400;500;700;800&display=swap">
<style>
  :root {
    --navy: #1c2f8e;
    --orange: #f08a24;
    --red: #e0284d;
    --paper: #ffffff;
    --backdrop: #c9ccd3;
    --ink: #1c2f8e;
  }
  html, body {
    margin: 0;
    width: 1200px;
    height: 878px;
    overflow: hidden;
    background: var(--backdrop);
    font-family: "Montserrat", sans-serif;
  }
  .sheet {
    width: 1200px;
    height: 878px;
    display: flex;
    flex-direction: column;
    align-items: center;
    justify-content: center;
    gap: 56px;
  }
  .card {
    position: relative;
    width: 580px;
    height: 332px;
    background: var(--paper);
    box-shadow: 0 6px 18px rgba(40, 45, 60, 0.18);
    overflow: hidden;
  }
  .brand {
    display: flex;
    align-items: center;
    gap: 10px;
    color: var(--navy);
    font-weight: 800;
    text-transform: uppercase;
    letter-spacing: 0.5px;
  }
  .brand-name { display: flex; flex-direction: column; line-height: 1.05; }
  .brand-dot {
    border-radius: 50%;
    background: var(--orange);
    flex: none;
  }
  /* front */
  .card-front .brand {
    position: absolute;
    left: 30px;
    top: 100px;
    font-size: 22px;
  }
  .card-front .brand-dot { width: 18px; height: 18px; }
  .owner {
    position: absolute;
    right: 30px;
    top: 30px;
    text-align: center;
    color: var(--navy);
  }
  .owner-name {
    font-weight: 800;
    font-size: 20px;
    text-transform: uppercase;
    letter-spacing: 0.4px;
  }
  .owner-title {
    font-size: 11px;
    letter-spacing: 5px;
    margin-top: 2px;
    font-weight: 500;
  }
  .contact {
    position: absolute;
    left: 250px;
    top: 92px;
    margin: 0;
    padding: 0;
    list-style: none;
    color: var(--ink);
    font-size: 13px;
    line-height: 22px;
  }
  .stripes {
    position: absolute;
    left: 0;
    top: 190px;
    width: 580px;
    height: 44px;
  }
  .services {
    position: absolute;
    left: 34px;
    right: 30px;
    top: 258px;
    display: flex;
    justify-content: space-between;
    margin: 0;
    padding: 0;
    list-style: none;
    color: var(--navy);
    font-size: 12px;
    font-weight: 500;
    letter-spacing: 0.8px;
    text-transform: uppercase;
  }
  .services li { display: flex; align-items: center; gap: 7px; }
  .services li::before {
    content: "";
    width: 6px;
    height: 6px;
    border-radius: 50%;
    border: 2px solid var(--orange);
    background: var(--red);
  }
  /* back */
  .card-back {
    display: flex;
    align-items: center;
    justify-content: center;
  }
  .card-back .brand { font-size: 30px; gap: 14px; }
  .card-back .brand-dot { width: 26px; height: 26px; }
</style>
</head>
<body>
<main class="sheet">
  <section class="card card-front" aria-label="Business card front">
    <div class="brand">
      <span class="brand-dot"></span>
      <span class="brand-name"><span>Breezeway</span><span>Comfort</span></span>
    </div>
    <div class="owner">
      <div class="owner-name">Marcus Tollefsen</div>
      <div class="owner-title">OWNER</div>
    </div>
    <ul class="contact">
      <li>L : 2874590</li>
      <li>P : 555-382-4071</li>
      <li>E : breezewaycomfortair@mailvista.example</li>
    </ul>
    <svg class="stripes" viewBox="0 0 580 44" aria-hidden="true">
      <defs>
        <linearGradient id="band" x1="0" x2="1" y1="0" y2="0">
          <stop offset="0" stop-color="#f08a24"/>
          <stop offset="0.55" stop-color="#ef6a2c"/>
          <stop offset="1" stop-color="#e0284d"/>
        </linearGradient>
      </defs>
      <rect x="270" y="2" width="310" height="3" fill="var(--navy)"/>
      <polygon points="200,30 210,10 580,8 580,30" fill="url(#band)"/>
      <rect x="30" y="36" width="550" height="3" fill="var(--navy)"/>
    </svg>
    <ul class="services">
      <li>Sales</li>
      <li>Service</li>
      <li>Installation</li>
      <li>Maintenance</li>
    </ul>
  </section>

  <section class="card card-back" aria-label="Business card back">
    <div class="brand"><span class="brand-dot"></span>Breezeway Comfort</div>
  </section>
</main>
</body>
</html>
```